Harbor Crest Physician Advising

I need a one-page advertisement that I can email to potential clients.

The target audience is hospital administrators.

I want it to include the logo, as attached. We specialize in Payer Denial Management. We are certified physician advisors with over 80 years combined clinical medicine experience. We have expertise in Utilization Management, Clinical Documentation Integrity, Peer to Peer Appeals and Letter Appeal Management. We win over 60% of our Peer to Peer Appeals with Medicare Advantage plans and over 50% of our first level letters.

We make sure hospitals get paid for the care they provide, I really want to emphasize that we are very effective at overturning insurance payment denials. We also provider other physician advising services. We keep our company small so that our rates are very affordable. Include that references are available.

We need to include: Contact us today, we can improve your revenue. Please 304-555-0183
or email (I will provide this later).

I want it to look professional but not bland, with maybe AI created images of a small group of physicians (mature, white coats, stethoscopes) looking at a spreadsheet on a laptop. a picture of a stack of money setting on a table, with a hand removing part of the money from the stack.

Companies like ours include Quorvix, T7, Pellingham, Car-Nova, and TelvanMD. Their websites may provide ideas.

Target Market(s)

Healthcare administrators who need to improve their hospital revenue

Industry/Entity Type

Healthcare consulting

Font styles to use
Sans Serif

Colors
0094D4
00A9DD
6FCCEA
C7EBF8
E9F6FB
00AB8E
00BBA5
67D7C9
C6EFE9
E9F9F6
FFC000
F8CF3A
FAE287
FDF2CF
FEFAEE
EE7325
F08F49
F5BC92
FAE3D3
FDF4ED
E54698
E96AAD
F1A4CE
F9D9EA
FCEFF6
6B429C
8869AF
B7A5CE
E3DAEB
F3F0F8

Requirements
Must have
• Must include that we are very successful here to appear in Peer to Peer appeals and Letter appeals
Nice to have
• Very easy to read, big bold fonts
Should not have
• I’m very afraid of having a lot of dark blues, combined with dark gold, because it may look like the colors of a health system in my area

```html
<!DOCTYPE html>
<html lang="en">
<head>
<meta charset="UTF-8">
<title>Harbor Crest Physician Advising</title>
<link href="https://fonts.googleapis.com/css2?family=Montserrat:wght@500;600;700;800;900&display=swap" rel="stylesheet">
<style>
:root{
  --navy:#0b2479;
  --blue-deep:#0f2f96;
  --blue:#1e4cc0;
  --blue-text:#1a3aa8;
  --green-dark:#3f7a1f;
  --green:#5a9e2c;
  --green-light:#72bb3a;
  --green-text:#3d7d1f;
  --ink:#1d1d1d;
  --footer:#272727;
  --white:#ffffff;
  --rule:#bcbcbc;
}
*{margin:0;padding:0;box-sizing:border-box}
html,body{width:940px;height:1200px;overflow:hidden;background:#fff}
body{font-family:"Montserrat",sans-serif;color:var(--ink)}
.flyer{position:relative;width:940px;height:1200px;overflow:hidden;background:var(--white)}
.hero-band{position:absolute;inset:0 0 auto 0;height:700px;
  background:linear-gradient(180deg,#0a2473 0%,#14389f 40%,#1f4fc2 100%);
  clip-path:polygon(0 0,940px 0,940px 689px,478px 689px,0 414px)}
.hero-photo{position:absolute;left:325px;top:234px;width:615px;height:455px;
  background:linear-gradient(160deg,#6f8fd6 0%,#c9d6ec 45%,#e9eef6 70%,#c7a778 100%);
  clip-path:polygon(0 0,615px 0,615px 455px,153px 455px,0 366px)}
.hero-rule{position:absolute;left:0;top:0;width:940px;height:700px;pointer-events:none}
.headline{position:absolute;left:0;width:940px;text-align:center;color:var(--white);font-weight:900;letter-spacing:-1px}
.headline.line1{top:30px;font-size:82px;line-height:90px}
.headline.line2{top:110px;font-size:64px;line-height:70px}
.tagline{position:absolute;left:0;top:176px;width:940px;text-align:center;color:var(--green-light);font-weight:600;font-size:38px}
.hex-left{position:absolute;left:56px;top:306px;width:276px;height:312px}
.hex-left .txt{position:absolute;left:0;width:276px;text-align:center}
.hex-left .spec{top:75px;color:#fff;font-weight:700;font-size:18px;line-height:20px}
.hex-left .paid{top:140px;color:#fff;font-weight:800;font-size:17px;line-height:20px}
.hex-left .loss{top:196px;color:#1b2a12;font-weight:500;font-size:21px;line-height:23px}
.hex-right{position:absolute;left:701px;top:247px;width:180px;height:204px}
.hex-right .txt{position:absolute;left:0;width:180px;text-align:center;color:#fff}
.hex-right .num{top:36px;font-size:48px;font-weight:700;line-height:50px}
.hex-right .yrs{top:82px;font-size:26px;font-weight:600;line-height:28px}
.hex-right .exp{top:116px;font-size:15px;font-weight:800;line-height:18px}
.results-title{position:absolute;left:65px;top:636px;color:var(--blue-text);font-weight:900;font-size:27px;line-height:28px}
.stat{position:absolute;left:65px;width:420px}
.stat .icon{position:absolute;left:0;top:0;width:54px;height:54px}
.stat .value{position:absolute;left:74px;top:-6px;color:var(--green-text);font-weight:700;font-size:46px;line-height:46px}
.stat .desc{position:absolute;left:76px;font-weight:600;font-size:13px;line-height:16px}
.stat-rule{position:absolute;left:140px;width:342px;border-top:1px dotted var(--rule)}
.team-note{position:absolute;left:65px;top:978px;width:350px;font-weight:700;font-size:13.5px;line-height:17.5px}
.team-note .hl{color:var(--green-text)}
.services-title{position:absolute;left:466px;top:728px;color:var(--blue-text);font-weight:900;font-size:26px}
.service{position:absolute;left:468px;width:393px;height:42px}
.service .pill{position:absolute;left:36px;top:0;width:357px;height:42px;border:2px solid var(--blue);border-left:none;border-radius:0 14px 14px 0;background:#fff}
.service.green .pill{border-color:var(--green-light)}
.service .dot{position:absolute;left:0;top:-2px;width:46px;height:46px;border-radius:50%;background:radial-gradient(circle at 35% 30%,#3c86e6,#1444b0)}
.service.green .dot{background:radial-gradient(circle at 35% 30%,#7cc84a,#3f8a22)}
.service .dot svg{position:absolute;left:11px;top:11px;width:24px;height:24px}
.service .label{position:absolute;left:60px;top:11px;font-weight:700;font-size:14.5px;color:#1b1b1b}
.footer{position:absolute;left:0;top:1072px;width:940px;height:128px;background:var(--footer);clip-path:polygon(325px 0,940px 0,940px 128px,249px 128px)}
.contact-lead{position:absolute;left:333px;top:1096px;font-weight:700;font-size:19.5px;color:var(--green-light)}
.contact-lead .blue{color:#3c8ef0}
.contact-line{position:absolute;left:333px;top:1130px;color:#fff;font-weight:700;display:flex;align-items:center}
.contact-line .phone{font-size:24px;margin-right:14px}
.contact-line .email{font-size:20px}
.contact-line svg{width:22px;height:22px;margin-right:8px}
.brand{position:absolute;left:40px;top:1085px;width:240px;text-align:center;color:#4a4a4a;font-weight:600}
.brand .mark{width:36px;height:36px;border-radius:50%;background:var(--green);margin:0 auto 6px}
.brand .name{font-size:20px;line-height:22px}
.brand .sub{font-size:11px;letter-spacing:1px;line-height:14px}
</style>
</head>
<body>
<main class="flyer">
  <div class="hero-band"></div>
  <div class="hero-photo" role="img" aria-label="Photo of three physicians in white coats with stethoscopes reviewing a laptop, a stack of money on the desk"></div>
  <svg class="hero-rule" viewBox="0 0 940 700">
    <polyline points="270,563 478,685 940,685" fill="none" stroke="#1a3ec0" stroke-width="7"/>
  </svg>

  <h1 class="headline line1">HARBOR CREST</h1>
  <h2 class="headline line2">PHYSICIAN ADVISING</h2>
  <p class="tagline">Certified Physician Advisors</p>

  <section class="hex-left">
    <svg width="276" height="312" viewBox="0 0 276 312">
      <defs>
        <clipPath id="hexClip"><polygon points="138,6 270,82 270,230 138,306 6,230 6,82"/></clipPath>
      </defs>
      <polygon points="138,0 276,79 276,233 138,312 0,233 0,79" fill="#3d7a1c"/>
      <g clip-path="url(#hexClip)">
        <rect x="0" y="0" width="276" height="133" fill="#4c8f23"/>
        <rect x="0" y="133" width="276" height="53" fill="#1c2675"/>
        <rect x="0" y="186" width="276" height="130" fill="#74b93c"/>
      </g>
    </svg>
    <p class="txt spec">WE SPECIALIZE<br>IN PAYER DENIAL<br>MANAGEMENT</p>
    <p class="txt paid">WE HELP HOSPITALS<br>GET PAID</p>
    <p class="txt loss">Insurance denials<br>cost your hospital<br>money.</p>
  </section>

  <section class="hex-right">
    <svg width="180" height="204" viewBox="0 0 180 204">
      <polygon points="90,0 180,51 180,153 90,204 0,153 0,51" fill="#5c9b2a"/>
      <polygon points="90,5 175,54 175,150 90,199 5,150 5,54" fill="#3f7a1f"/>
    </svg>
    <p class="txt num">80+</p>
    <p class="txt yrs">YEARS</p>
    <p class="txt exp">OF CLINICAL<br>EXPERIENCE</p>
  </section>

  <h3 class="results-title">WE OVERTURN<br>THEM - WITH<br>RESULTS THAT MATTER:</h3>

  <div class="stat" style="top:742px">
    <svg class="icon" viewBox="0 0 54 54">
      <path d="M27 2 l9 4 v8 c0 6-4 10-9 12 c-5-2-9-6-9-12 v-8z" fill="#1a3aa8"/>
      <path d="M22 13 l4 4 l7-7" stroke="#fff" stroke-width="2.5" fill="none"/>
      <circle cx="14" cy="34" r="9" fill="#3d7d1f"/>
      <path d="M10 34 l3 3 l6-6" stroke="#fff" stroke-width="2" fill="none"/>
      <rect x="28" y="28" width="16" height="18" rx="3" fill="#3d7d1f"/>
      <path d="M9 42 l-3 9 l6-3 M19 42 l3 9 l-6-3" fill="#3d7d1f"/>
    </svg>
    <p class="value">60%+</p>
    <p class="desc" style="top:42px">Success rate in Peer-to-Peer<br>appeals (Medicare Advantage)</p>
  </div>
  <div class="stat-rule" style="top:816px"></div>

  <div class="stat" style="top:830px">
    <svg class="icon" viewBox="0 0 54 54">
      <rect x="2" y="40" width="7" height="12" fill="#3d7d1f"/>
      <rect x="12" y="34" width="7" height="18" fill="#3d7d1f"/>
      <rect x="22" y="28" width="7" height="24" fill="#3d7d1f"/>
      <rect x="32" y="18" width="7" height="34" fill="#3d7d1f"/>
      <rect x="42" y="8" width="7" height="44" fill="#1a3aa8"/>
      <circle cx="14" cy="10" r="4" fill="#1a3aa8"/>
      <path d="M14 15 v10 M8 20 h12 M14 25 l-5 7 M14 25 l5 7" stroke="#1a3aa8" stroke-width="3"/>
    </svg>
    <p class="value">50%+</p>
    <p class="desc" style="top:40px">Success rate in First-Level<br>Letter Appeals</p>
  </div>
  <div class="stat-rule" style="top:904px"></div>

  <div class="stat" style="top:906px">
    <svg class="icon" viewBox="0 0 54 54">
      <circle cx="27" cy="8" r="7" fill="#1a3aa8"/>
      <path d="M23 8 l3 3 l5-5" stroke="#fff" stroke-width="2" fill="none"/>
      <circle cx="12" cy="24" r="5" fill="#1a3aa8"/>
      <circle cx="42" cy="24" r="5" fill="#1a3aa8"/>
      <circle cx="27" cy="28" r="6" fill="#3d7d1f"/>
      <path d="M3 44 c0-9 18-9 18 0z M33 44 c0-9 18-9 18 0z" fill="#1a3aa8"/>
      <path d="M16 52 c0-14 22-14 22 0z" fill="#3d7d1f"/>
      <path d="M27 42 v7 M23.5 45.5 h7" stroke="#fff" stroke-width="2"/>
    </svg>
    <p class="desc" style="top:12px">Affordable, physician-led services<br>tailored to your needs</p>
  </div>

  <p class="team-note">We’re a small, expert team— <span class="hl">which means lower rates, faster turnaround, and personalized service.</span> References available.</p>

  <h3 class="services-title">WHAT WE DO BEST</h3>

  <div class="service" style="top:776px">
    <div class="pill"></div>
    <div class="dot"><svg viewBox="0 0 24 24"><circle cx="8" cy="7" r="3" fill="#fff"/><circle cx="16" cy="15" r="3" fill="#fff"/><path d="M3 14 a5 5 0 0 1 5-4 M21 8 a5 5 0 0 0-5 2" stroke="#fff" stroke-width="2" fill="none"/></svg></div>
    <span class="label">Peer-to-Peer Appeals</span>
  </div>
  <div class="service green" style="top:828px">
    <div class="pill"></div>
    <div class="dot"><svg viewBox="0 0 24 24"><rect x="5" y="3" width="14" height="18" rx="2" fill="#fff"/><path d="M12 9 v7 M8.5 12.5 h7" stroke="#3f8a22" stroke-width="2"/></svg></div>
    <span class="label">Letter Appeal Management</span>
  </div>
  <div class="service" style="top:880px">
    <div class="pill"></div>
    <div class="dot"><svg viewBox="0 0 24 24"><circle cx="12" cy="12" r="8" stroke="#fff" stroke-width="3" stroke-dasharray="4 2" fill="none"/><circle cx="12" cy="10" r="2.5" fill="#fff"/><path d="M8 16 c0-4 8-4 8 0z" fill="#fff"/></svg></div>
    <span class="label">Utilization Management (UM)</span>
  </div>
  <div class="service green" style="top:931px">
    <div class="pill"></div>
    <div class="dot"><svg viewBox="0 0 24 24"><circle cx="10" cy="7" r="4" fill="#fff"/><path d="M2 21 c0-8 14-8 14 0z" fill="#fff"/><circle cx="18" cy="17" r="3" stroke="#fff" stroke-width="2" fill="none"/></svg></div>
    <span class="label">Clinical Documentation Integrity (CDI)</span>
  </div>
  <div class="service" style="top:983px">
    <div class="pill"></div>
    <div class="dot"><svg viewBox="0 0 24 24"><circle cx="12" cy="8" r="4" fill="#fff"/><path d="M4 22 c0-9 16-9 16 0z" fill="#fff"/><path d="M12 1 v4 M10 3 h4" stroke="#fff" stroke-width="1.5"/></svg></div>
    <span class="label">Physician Advising Services</span>
  </div>

  <div class="brand">
    <div class="mark"></div>
    <p class="name">HARBOR CREST</p>
    <p class="sub">PHYSICIAN ADVISING</p>
  </div>

  <div class="footer"></div>
  <p class="contact-lead">Contact us today. <span class="blue">Let’s Recover Your Revenue</span></p>
  <div class="contact-line">
    <svg viewBox="0 0 22 22"><circle cx="11" cy="11" r="10" fill="#1e5fd6" stroke="#fff" stroke-width="1.5"/><path d="M7 6 l2 0 l1 3 l-1.5 1 c1 2 2 3 3.5 3.5 l1-1.5 l3 1 v2 c-5 1-10-4-9-9z" fill="#fff"/></svg>
    <span class="phone">304-555-0183</span>
    <svg viewBox="0 0 22 22"><circle cx="11" cy="11" r="10" fill="#1e5fd6" stroke="#fff" stroke-width="1.5"/><rect x="6" y="7.5" width="10" height="7" rx="1" fill="#fff"/><path d="M6 8 l5 4 l5-4" stroke="#1e5fd6" stroke-width="1.2" fill="none"/></svg>
    <span class="email">info@harborcrestadvising.com</span>
  </div>
</main>
</body>
</html>
```